Bramblecrest Roofing Co. business card design

I am a Roofing contractor in Texas. The name of my company is Bramblecrest Roofing Co. I also offer a few other services (Christmas light installation, gutters, fencing, pressure washing). However my main gig is roofing. Storm restoration and knowledge of the insurance claim process is my specialty.

My colors are black, red and white. I’d like something pretty simple and clean. Modern looking but with a splash of this red tartan pattern.

I have another version of my logo being edited at the moment where the little top part of the F in roofing that’s currently tartan will be changed to just solid red to make it more visible. So if that’s something you can change in your mock up great. But I can provide the full version once the contest is complete

Target Market(s)

Homeowners

Industry/Entity Type

Roofing

Contact Information for Business Card

Darren Pike. 682-555-0193. www.bramblecrest roofing.example Darren@bramblecrestroofing.example

Colors
EB3D1F
EC4F4E
F09395
F8D3D4
FCEDEE

Requirements
Nice to have
• Maybe instead of a business address. I could say serving all DFW Texas or something like that. And maybe add a line somewhere saying deductible assistance? Just a thought

```html
<!DOCTYPE html>
<html lang="en">
<head>
<meta charset="utf-8">
<title>Bramblecrest Roofing Co. – Business Card</title>
<link href="https://fonts.googleapis.com/css2?family=Michroma&family=Open+Sans:wght@400;500&display=swap" rel="stylesheet">
<style>
  :root {
    --bg: #d3d4d6;
    --card: #ffffff;
    --red: #e0222a;
    --red-deep: #6b0f10;
    --black: #111111;
    --ink: #1a1a1a;
  }
  * { margin: 0; padding: 0; box-sizing: border-box; }
  html, body { width: 900px; height: 1200px; overflow: hidden; background: var(--bg); }
  .canvas { position: relative; width: 900px; height: 1200px; }

  .card {
    position: absolute; left: 121px; width: 658px; height: 375px;
    border-radius: 14px; overflow: hidden; background: var(--card);
  }
  .card--front { top: 204px; }
  .card--back { top: 621px; }

  .tartan-field {
    position: absolute; inset: 0;
    background:
      linear-gradient(180deg, var(--red-deep) 0%, var(--red) 30%, #f2f2f2 40%, var(--red) 50%, var(--black) 70%, var(--red) 85%, var(--red-deep) 100%);
  }
  .front-name {
    position: absolute; inset: 0; display: flex; align-items: center; justify-content: center;
    font-family: "Michroma", sans-serif; font-size: 22px; color: #ffffff;
    letter-spacing: 1px; text-align: center;
  }

  .brand { position: absolute; top: 44px; left: 0; right: 0; text-align: center; }
  .brand-dot {
    width: 100px; height: 100px; border-radius: 50%; background: var(--red);
    margin: 0 auto 22px;
  }
  .brand-name {
    font-family: "Michroma", sans-serif; font-size: 20px; line-height: 26px;
    color: var(--red); text-transform: uppercase;
  }

  .holder {
    position: absolute; top: 272px; right: 353px; text-align: right;
  }
  .holder-name { font-family: "Michroma", sans-serif; font-size: 22px; line-height: 26px; }
  .holder-name .first { color: var(--red); }
  .holder-name .last { color: var(--black); }
  .holder-role {
    font-family: "Open Sans", sans-serif; font-size: 15px; color: var(--red);
    margin-top: 2px; letter-spacing: .5px;
  }

  .divider { position: absolute; left: 329px; top: 262px; width: 1.5px; height: 71px; background: var(--black); }

  .contacts { position: absolute; left: 351px; top: 260px; list-style: none; }
  .contacts li {
    display: flex; align-items: center; gap: 6px; height: 25.5px;
    font-family: "Open Sans", sans-serif; font-size: 15px; color: var(--ink);
  }
  .contacts .phone { letter-spacing: 2.5px; }
  .contacts svg { width: 14px; height: 14px; flex: none; }

  .tartan-strip { position: absolute; left: 0; right: 0; bottom: 0; height: 14px;
    background: linear-gradient(90deg, var(--red-deep), var(--red), var(--black), var(--red), var(--red-deep)); }
</style>
</head>
<body>
<div class="canvas">
  <section class="card card--front">
    <div class="tartan-field" role="img" aria-label="Red, black and white tartan pattern"></div>
    <div class="front-name">Bramblecrest Roofing Co.</div>
  </section>

  <section class="card card--back">
    <div class="brand">
      <div class="brand-dot"></div>
      <div class="brand-name">Bramblecrest<br>Roofing Co.</div>
    </div>

    <div class="holder">
      <div class="holder-name"><span class="first">DARREN</span> <span class="last">PIKE</span></div>
      <div class="holder-role">OWNER</div>
    </div>

    <div class="divider"></div>

    <ul class="contacts">
      <li class="phone">
        <svg viewBox="0 0 24 24"><path fill="#e0222a" d="M6.6 10.8a15.5 15.5 0 0 0 6.6 6.6l2.2-2.2c.3-.3.7-.4 1-.2 1.1.4 2.3.6 3.6.6.6 0 1 .4 1 1V20c0 .6-.4 1-1 1A17 17 0 0 1 3 4c0-.6.4-1 1-1h3.5c.6 0 1 .4 1 1 0 1.3.2 2.5.6 3.6.1.3 0 .7-.2 1z"/></svg>
        682-555-0193
      </li>
      <li>
        <svg viewBox="0 0 24 24"><rect x="2" y="5" width="20" height="14" fill="#e0222a"/><path d="M2 5l10 8 10-8" fill="none" stroke="#fff" stroke-width="1.6"/></svg>
        Darren@bramblecrestroofing.example
      </li>
      <li>
        <svg viewBox="0 0 24 24"><g fill="none" stroke="#e0222a" stroke-width="2"><circle cx="12" cy="12" r="9"/><ellipse cx="12" cy="12" rx="4" ry="9"/><path d="M3 12h18M5 7h14M5 17h14"/></g></svg>
        www.bramblecrestroofing.example
      </li>
    </ul>

    <div class="tartan-strip" role="img" aria-label="Thin band of red tartan pattern"></div>
  </section>
</div>
</body>
</html>
```